KETRAV Website - Innovative Products need a creative designer!

I require a bold, fun and interactive website designing for my company rebrand. I am in the process of having new logo's designed but the colour scheme is already established.

Colours: Yellow (PRIMARY) : #C6FF02 / RGB: 198, 255, 2 Black (SECONDARY): #000000 / RGB: 0, 0, 0

The company specialises in Temporary Modular Space, so i would like to see creative blocks illustrating the products. (Products listed below). Please only design the homepage and the winner will then design / code the full thing. Please include an area that elaborates on the sustainablity factor of the company. I like animated emblems, pictures and writing. There will be on going work on this, as I will need the designer to provide up keep and maintenance on it as we progress.

Menu Pages:

The Solutions - (Products):
Wandlock: An innovative point of sale units specifically designed for the sale of Merchandise. It transports like a normal shipping container, but once situated expands outwards to increase the internal footprint by up to 90%. And once in situ are completely antivandal, removing the requirement for multiple security personnel and protecting your products. It also provide sales points to a 180 degree angle, maximising revenue and reducing queue time. - Completely customisable.

Roostel: A penthouse in a box, the innovative nature of the unit enables it to be situated anywhere. Ideal for glamping sites, guest houses at private properties for temporary Festival accommodation. The unit comes fully furnished with a kitchenette, en suite bathroom and ample space for a double bed and a living area. This is truly the luxurious and affordable option for temporary accommodation.

Glimcase: A standalone product, but also an accessory to the Wandlock. A flat pack system that is truly 100% modular, all wall panels can be installed tailored to your requirements. This can be an on site office, or a glass display box for brand activations. Installed on the ground or on the roof of the Wandlock, it is a flexible piece of equipment designed that is not only premium but affordable. - Completely customisable.

PLRange:
PL10: A quick install and sustainable design for use on a variety of sites. The cabins collapse down enabling multiple units to be transported on a 1no. truck. We can transport 20no. units on 1no. 40ft truck, reducing the carbon footprint of events drastically. When erected, they can be stacked to create 2no. floors. - Completely customisable.
PL20: Same as the above but a 20ft cabin. These can transport 10no. units on a 40ft trailer. Can be stacked to create 2no. floors. - Completely customisable.

The Industries:
Merchandise & Shows
Sports & Stadia
Brand Activations
Retail & Stores
Events & Festivals
Automotive
Exhibitions

The Company: Will confirm all information once the winner is selected.

Contact: Will confirm all information once the winner is selected.

Events, Merchandise, Stadiums, Automotive, Brand Activations, Commercial

Must have
• Interactive elements, engaging design, innovative movements, be bright and bold. But most importantly be informative and easy to navigate.
Nice to have
• Animations of blocks, moving emblems.
Should not have
• No pre existing templates

```html
<!DOCTYPE html>
<html lang="en">
<head>
<meta charset="utf-8">
<title>KETRAV – Temporary Modular Space</title>
<link href="https://fonts.googleapis.com/css2?family=Rajdhani:wght@600;700&family=Roboto:wght@400;500;700&display=swap" rel="stylesheet">
<style>
:root{
  --lime:#C6FF02;
  --lime-soft:#eefcc0;
  --black:#000;
  --ink:#111;
  --text:#666;
  --grey-bg:#f2f2f2;
  --footer:#222;
  --white:#fff;
}
*{margin:0;padding:0;box-sizing:border-box}
html,body{width:1200px;height:3672px;overflow:hidden}
body{position:relative;font-family:"Roboto",sans-serif;color:var(--ink);background:var(--white)}
.abs{position:absolute}
.heading{font-family:"Rajdhani",sans-serif;font-weight:700;letter-spacing:1px;text-transform:uppercase}
.btn{position:absolute;display:flex;align-items:center;gap:12px;justify-content:center;background:var(--lime);color:var(--black);font-weight:700;font-size:14px;text-transform:uppercase;border-radius:2px;text-decoration:none}
.btn .ring{width:20px;height:14px;border:2px solid rgba(0,0,0,.25);border-radius:8px}

/* top bar */
.topbar{left:0;top:0;width:1200px;height:36px;background:var(--black);color:var(--white);font-size:13px}
.topbar .item{position:absolute;top:10px;display:flex;align-items:center;gap:8px}
.topbar .sep{position:absolute;left:384px;top:6px;width:1px;height:24px;background:#2b6cff}
.flag{width:20px;height:20px;border-radius:50%;background:#9fb3d9}

/* nav */
.nav{left:0;top:36px;width:1200px;height:79px;background:var(--white)}
.brand{position:absolute;display:flex;align-items:center;gap:12px;font-family:"Rajdhani",sans-serif;font-weight:700;font-size:34px;letter-spacing:1px}
.brand .mark{width:34px;height:34px;background:currentColor}
.nav .links a{position:absolute;top:28px;font-size:14px;font-weight:500;color:var(--ink);text-decoration:none}
.nav .links a.active::after{content:"";position:absolute;left:0;right:0;bottom:-14px;height:3px;background:var(--lime)}

/* hero */
.hero-photo{left:0;top:115px;width:1200px;height:625px}
.hero-title{left:143px;top:252px;font-size:68px;color:var(--white);letter-spacing:2px}
.hero-sub{left:143px;top:342px;font-size:16px;font-weight:500;color:var(--white)}
.dots{position:absolute;display:flex;gap:4px}
.dots span{width:11px;height:11px;border-radius:50%;border:1.5px solid #999;background:transparent}
.dots span.on{background:var(--lime);border-color:var(--lime)}
.hero .dots span{border-color:var(--white)}

/* sustainability */
.sus-frame{left:128px;top:945px;width:318px;height:299px;border:4px solid var(--lime)}
.sus-photo{left:144px;top:831px;width:429px;height:396px;background:linear-gradient(180deg,#b9bcc3 0%,#7b7f88 45%,#3d3a3f 100%)}
.sus-accent{left:466px;top:805px;width:134px;height:136px;background:var(--lime-soft)}
.sus-title{left:640px;top:846px;width:440px;font-size:33px;line-height:47px;color:var(--black)}
.sus-copy{left:640px;top:946px;width:418px;font-size:13px;line-height:23px;color:var(--text)}
.sus-copy p+p{margin-top:8px}

/* solutions */
.solutions{left:0;top:1304px;width:1200px;height:731px;background:var(--black)}
.sec-title{position:absolute;left:0;width:1200px;text-align:center;font-size:34px}
.side-card{top:1458px;height:353px;background:linear-gradient(135deg,#2a2a2a,#141414)}
.main-card{left:370px;top:1442px;width:461px;height:386px;border:3px solid var(--lime);box-shadow:0 0 22px rgba(198,255,2,.55);background:linear-gradient(180deg,#4d6f76 0%,#b7bccb 55%,#cfcbe0 100%)}
.main-card .label{position:absolute;left:171px;bottom:14px;width:112px;height:35px;background:#7a7a86;color:var(--white);font-size:17px;display:flex;align-items:center;justify-content:center}
.sol-copy{left:143px;top:1864px;width:914px;text-align:center;color:var(--white);font-size:13.6px;line-height:24px}

/* range */
.range-bg{left:0;top:2035px;width:1200px;height:469px;background:var(--grey-bg)}
.range-photo{left:0;top:2035px;width:1200px;height:469px}
.range-title{left:143px;top:2092px;font-size:33px;color:var(--black)}
.range-copy{left:143px;top:2146px;width:392px;font-size:13.4px;line-height:24px;color:var(--text)}
.range-copy b{font-size:17px;font-weight:500;color:var(--black)}
.range-copy p+p{margin-top:4px}

/* industries */
.ind-title{top:2578px;color:var(--black)}
.card{position:absolute;width:287px;height:240px;background:var(--white);box-shadow:0 2px 14px rgba(0,0,0,.09);text-align:center}
.card.lift{box-shadow:0 4px 20px rgba(0,0,0,.16)}
.card svg{position:absolute;left:108px;top:28px}
.card h3{position:absolute;left:0;right:0;top:112px;font-size:17px;font-weight:500;color:var(--black)}
.card p{position:absolute;left:20px;right:20px;top:145px;font-size:13px;line-height:23px;color:var(--text)}

/* footer */
.footer-bg{left:0;top:3260px;width:1200px;height:412px}
.footer{color:var(--white)}
.f-head{position:absolute;font-family:"Roboto",sans-serif;font-weight:700;font-size:17px;text-transform:uppercase}
.f-links a{position:absolute;left:397px;font-size:11px;color:var(--white);text-decoration:none}
.contact-row{position:absolute;left:565px;display:flex;gap:12px;align-items:flex-start;font-size:11px;line-height:19px}
.contact-row .ic{flex:none;width:20px;height:20px;border-radius:50%;background:#3a3a3a;display:flex;align-items:center;justify-content:center}
.sub-copy{left:817px;top:3442px;width:230px;font-size:11px;line-height:19px}
.sub-form{left:817px;top:3494px;width:236px;height:33px;background:var(--white);border-radius:2px}
.sub-form .ph{position:absolute;left:12px;top:10px;font-size:10px;color:#999}
.sub-form .go{position:absolute;right:0;top:0;width:44px;height:33px;background:var(--lime);display:flex;align-items:center;justify-content:center}
.social{position:absolute;top:3549px;width:27px;height:27px;border-radius:50%;border:1px solid #555;background:#2e2e2e}
.f-rule{left:143px;top:3615px;width:913px;height:1px;background:#3c3c3c}
.f-bottom{top:3634px;font-size:12px}
.f-bottom u{text-decoration:underline}
</style>
</head>
<body>

<!-- top bar -->
<div class="abs topbar">
  <div class="item" style="left:143px">
    <svg width="12" height="12" viewBox="0 0 24 24"><path fill="#fff" d="M6.6 10.8a15 15 0 0 0 6.6 6.6l2.2-2.2c.3-.3.7-.4 1-.2 1.1.4 2.3.6 3.6.6.6 0 1 .4 1 1V20c0 .6-.4 1-1 1A17 17 0 0 1 3 4c0-.6.4-1 1-1h3.5c.6 0 1 .4 1 1 0 1.2.2 2.4.6 3.6.1.3 0 .7-.2 1z"/></svg>
    <span>Call Us : <b>+1-555-014-2290</b></span>
  </div>
  <div class="sep"></div>
  <div class="item" style="left:425px">
    <svg width="13" height="11" viewBox="0 0 26 20"><rect x="1" y="1" width="24" height="18" rx="2" fill="#fff"/><path d="M2 3l11 8 11-8" stroke="#000" stroke-width="2" fill="none"/></svg>
    <span>info@ketrav.com</span>
  </div>
  <div class="item" style="left:965px;top:7px"><div class="flag"></div><span>English</span>
    <svg width="8" height="5" viewBox="0 0 8 5"><path d="M0 0h8L4 5z" fill="#fff"/></svg></div>
</div>

<!-- nav -->
<div class="abs nav">
  <div class="brand" style="left:143px;top:18px;color:var(--black)"><div class="mark" style="border-radius:4px"></div>KETRAV</div>
  <nav class="links">
    <a href="#" class="active" style="left:493px">Home</a>
    <a href="#" style="left:567px">The Solutions</a>
    <a href="#" style="left:692px">PLRange</a>
    <a href="#" style="left:787px">The Industries</a>
  </nav>
  <a class="btn" style="left:928px;top:18px;width:128px;height:39px;text-transform:none;font-weight:500;font-size:14px">Contact Us <span class="ring"></span></a>
</div>

<!-- hero -->
<section class="hero">
  <svg class="abs hero-photo" width="1200" height="625" viewBox="0 0 1200 625" role="img" aria-label="Dark modular container cabin with glass extension, set among trees">
    <defs><linearGradient id="heroG" x1="0" y1="0" x2="1" y2="1">
      <stop offset="0" stop-color="#8a8f8c"/><stop offset=".45" stop-color="#3c3e3d"/><stop offset="1" stop-color="#5a4f43"/></linearGradient></defs>
    <polygon points="0,0 1200,0 1200,510 600,600 0,510" fill="url(#heroG)"/>
    <polygon points="155,540 600,625 1045,540 600,585" fill="var(--lime)"/>
  </svg>
  <h1 class="abs heading hero-title">KETRAV</h1>
  <p class="abs hero-sub">The company specialises in Temporary Modular Space.</p>
  <a class="btn" style="left:143px;top:386px;width:179px;height:47px;font-size:15px">Get Started <span class="ring"></span></a>
  <div class="dots" style="left:578px;top:664px"><span></span><span></span><span></span></div>
</section>

<!-- sustainability -->
<section>
  <div class="abs sus-frame"></div>
  <div class="abs sus-accent" role="img" aria-label="Decorative accent area behind the photo"></div>
  <div class="abs sus-photo" role="img" aria-label="Merchandise container units set between city buildings"></div>
  <h2 class="abs heading sus-title">Sustainability Factor of the Company</h2>
  <div class="abs sus-copy">
    <p>Lorem ipsum dolor sit amet, consectetur adipiscing elit, sed do eiusmod tempor incididunt ut labore et dolore magna aliqua. Ut enim ad minim veniam, quis nostrud exercitation ullamco laboris nisi ut aliquip ex ea commodo consequat.</p>
    <p>Sed ut perspiciatis unde omnis iste natus error sit voluptatem accusantium doloremque laudantium, totam rem aperiam, eaque ipsa quae ab illo inventore veritatis et quasi architecto beatae vitae dicta sunt explicabo. Nemo enim ipsam voluptatem quia voluptas.</p>
  </div>
  <a class="btn" style="left:640px;top:1163px;width:151px;height:38px;font-size:13px">Learn More <span class="ring"></span></a>
</section>

<!-- solutions -->
<section>
  <div class="abs solutions"></div>
  <h2 class="heading sec-title" style="top:1374px;color:var(--white)">The Solutions</h2>
  <div class="abs side-card" style="left:0;width:346px" role="img" aria-label="Interior of a furnished accommodation unit"></div>
  <div class="abs side-card" style="left:852px;width:348px" role="img" aria-label="Glass display case housing a car"></div>
  <div class="abs main-card" role="img" aria-label="Expanded merchandise unit serving visitors outside a stadium">
    <div class="label">Wandlock</div>
  </div>
  <p class="abs sol-copy">An innovative point of sale units specifically designed for the sale of Merchandise. It transports like a normal shipping container, but once situated expands outwards to increase the internal footprint by up to 90%. And once in situ are completely antivandal, removing the requirement for multiple security personnel and protecting your products. It also provide sales points to a 180 degree angle, maximising revenue and reducing queue time. - Completely customisable.</p>
</section>

<!-- PL range -->
<section>
  <div class="abs range-bg"></div>
  <svg class="abs range-photo" width="1200" height="469" viewBox="0 0 1200 469" role="img" aria-label="Stacked blue cabins with external staircase inside a hall">
    <defs><linearGradient id="rangeG" x1="0" y1="0" x2="1" y2="1">
      <stop offset="0" stop-color="#3a3f6e"/><stop offset=".5" stop-color="#2a38a8"/><stop offset="1" stop-color="#1d2670"/></linearGradient></defs>
    <polygon points="627,0 1200,0 1200,469 563,469" fill="url(#rangeG)"/>
    <polygon points="617,0 626,0 598,150 589,150" fill="var(--lime)"/>
    <polygon points="582,196 590,196 557,469 549,469" fill="var(--black)"/>
  </svg>
  <h2 class="abs heading range-title">PL Range</h2>
  <div class="abs range-copy">
    <p><b>PL10:</b> A quick install and sustainable design for use on a variety of sites. The cabins collapse down enabling multiple units to be transported on a 1no. truck. We can transport 20no. units on 1no. 40ft truck, reducing the carbon footprint of events drastically. When erected, they can be stacked to create 2no. floors. - Completely customisable.</p>
    <p><b>PL20:</b> Same as the above but a 20ft cabin. These can transport 10no. units on a 40ft trailer. Can be stacked to create 2no. floors. - Completely customisable</p>
  </div>
  <a class="btn" style="left:144px;top:2396px;width:151px;height:38px;font-size:13px">Learn More <span class="ring"></span></a>
</section>

<!-- industries -->
<section>
  <h2 class="heading sec-title ind-title">The Industries</h2>

  <div class="card" style="left:145px;top:2646px">
    <svg width="70" height="70" viewBox="0 0 70 70"><circle cx="20" cy="50" r="17" fill="var(--lime)"/><rect x="18" y="10" width="46" height="46" fill="none" stroke="#111" stroke-width="2"/><path d="M34 10v12h14V10M34 16h14" fill="none" stroke="#111" stroke-width="2"/></svg>
    <h3>Merchandise &amp; Shows</h3>
    <p>Lorem ipsum dolor sit amet, consectetur adipiscing elit, Sed do eiusmod tempor incididunt.</p>
  </div>
  <div class="card lift" style="left:456px;top:2646px">
    <svg width="70" height="70" viewBox="0 0 70 70"><circle cx="20" cy="50" r="15" fill="var(--lime)"/><path d="M26 8h26v14a13 13 0 0 1-26 0z" fill="none" stroke="#111" stroke-width="2"/><circle cx="39" cy="18" r="6" fill="none" stroke="#111" stroke-width="2"/><path d="M39 35v10M30 45h18v8H30zM24 55h40" fill="none" stroke="#111" stroke-width="2"/></svg>
    <h3>Sports &amp; Stadia</h3>
    <p>Lorem ipsum dolor sit amet, consectetur adipiscing elit, Sed do eiusmod tempor incididunt.</p>
  </div>
  <div class="card" style="left:768px;top:2646px">
    <svg width="70" height="70" viewBox="0 0 70 70"><circle cx="20" cy="50" r="14" fill="var(--lime)"/><circle cx="38" cy="26" r="20" fill="none" stroke="#111" stroke-width="2"/><circle cx="38" cy="26" r="12" fill="none" stroke="#111" stroke-width="2"/><path d="M38 19l2.5 5 5.5.7-4 3.8 1 5.5-5-2.7-5 2.7 1-5.5-4-3.8 5.5-.7z" fill="none" stroke="#111" stroke-width="1.6"/><path d="M26 42l-8 18 7-2 4 6 6-16M50 42l8 18-7-2-4 6-6-16" fill="none" stroke="#111" stroke-width="2"/></svg>
    <h3>Brand Activations</h3>
    <p>Lorem ipsum dolor sit amet, consectetur adipiscing elit, Sed do eiusmod tempor incididunt.</p>
  </div>

  <div class="card" style="left:145px;top:2911px">
    <svg width="70" height="70" viewBox="0 0 70 70"><circle cx="20" cy="50" r="14" fill="var(--lime)"/><path d="M30 62V20h16v42M46 30h14v32M36 12h6v8M20 62h44" fill="none" stroke="#111" stroke-width="2"/><path d="M35 28h2M40 28h2M35 36h2M40 36h2M35 44h2M40 44h2M51 38h2M51 46h2" stroke="#111" stroke-width="2"/></svg>
    <h3>Retail &amp; Stores</h3>
    <p>Lorem ipsum dolor sit amet, consectetur adipiscing elit, Sed do eiusmod tempor incididunt.</p>
  </div>
  <div class="card" style="left:456px;top:2911px">
    <svg width="70" height="70" viewBox="0 0 70 70"><circle cx="20" cy="50" r="14" fill="var(--lime)"/><rect x="8" y="14" width="56" height="46" fill="none" stroke="#111" stroke-width="2"/><path d="M8 24h56M20 8v12M52 8v12" stroke="#111" stroke-width="2"/><path d="M36 31l3 6 6.5.8-4.8 4.5 1.2 6.5-5.9-3.2-5.9 3.2 1.2-6.5-4.8-4.5 6.5-.8z" fill="none" stroke="#111" stroke-width="1.8"/></svg>
    <h3>Events &amp; Festivals</h3>
    <p>Lorem ipsum dolor sit amet, consectetur adipiscing elit, Sed do eiusmod tempor incididunt.</p>
  </div>
  <div class="card" style="left:768px;top:2911px">
    <svg width="70" height="70" viewBox="0 0 70 70"><circle cx="22" cy="48" r="15" fill="var(--lime)"/><circle cx="38" cy="32" r="26" fill="none" stroke="#111" stroke-width="2"/><circle cx="38" cy="32" r="18" fill="none" stroke="#111" stroke-width="2"/><path d="M38 20v12l8 6" fill="none" stroke="#111" stroke-width="2"/></svg>
    <h3>Automotive</h3>
    <p>Lorem ipsum dolor sit amet, consectetur adipiscing elit, Sed do eiusmod tempor incididunt.</p>
  </div>

  <div class="dots" style="left:578px;top:3180px"><span></span><span class="on"></span><span></span></div>
</section>

<!-- footer -->
<footer class="footer">
  <svg class="abs footer-bg" width="1200" height="412" viewBox="0 0 1200 412">
    <polygon points="155,113 600,20 1045,113 600,62" fill="var(--lime)"/>
    <polygon points="0,118 600,78 1200,118 1200,412 0,412" fill="var(--footer)"/>
  </svg>

  <div class="brand" style="left:143px;top:3472px;color:var(--white)"><div class="mark" style="width:32px;height:32px;border-radius:4px"></div>KETRAV</div>

  <h4 class="f-head" style="left:397px;top:3400px">Quick Links</h4>
  <div class="f-links">
    <a href="#" style="top:3443px">Home</a>
    <a href="#" style="top:3467px">The Solutions</a>
    <a href="#" style="top:3491px">PLRange</a>
    <a href="#" style="top:3515px">The Industries</a>
  </div>

  <h4 class="f-head" style="left:568px;top:3400px">Contact Us</h4>
  <div class="contact-row" style="top:3449px"><span class="ic"><svg width="9" height="9" viewBox="0 0 24 24"><path fill="#fff" d="M6.6 10.8a15 15 0 0 0 6.6 6.6l2.2-2.2c.3-.3.7-.4 1-.2 1.1.4 2.3.6 3.6.6.6 0 1 .4 1 1V20c0 .6-.4 1-1 1A17 17 0 0 1 3 4c0-.6.4-1 1-1h3.5c.6 0 1 .4 1 1 0 1.2.2 2.4.6 3.6.1.3 0 .7-.2 1z"/></svg></span><span>+1-555-014-2290</span></div>
  <div class="contact-row" style="top:3488px"><span class="ic"><svg width="10" height="8" viewBox="0 0 26 20"><rect x="1" y="1" width="24" height="18" rx="2" fill="#fff"/><path d="M2 3l11 8 11-8" stroke="#3a3a3a" stroke-width="2" fill="none"/></svg></span><span>sales@ketrav.co.uk</span></div>
  <div class="contact-row" style="top:3526px"><span class="ic"><svg width="8" height="11" viewBox="0 0 16 22"><path d="M8 0a8 8 0 0 1 8 8c0 6-8 14-8 14S0 14 0 8a8 8 0 0 1 8-8z" fill="#fff"/><circle cx="8" cy="8" r="3" fill="#3a3a3a"/></svg></span><span>Lorem ipsum dolor sit amet,<br>consectetur adipiscing elit 651.</span></div>
  <div class="contact-row" style="top:3575px"><span class="ic"><svg width="10" height="10" viewBox="0 0 20 20"><circle cx="10" cy="10" r="8" fill="none" stroke="#fff" stroke-width="2"/><path d="M2 10h16M10 2c3 3 3 13 0 16M10 2c-3 3-3 13 0 16" fill="none" stroke="#fff" stroke-width="1.5"/></svg></span><span>www.ketrav.co.uk</span></div>

  <h4 class="f-head" style="left:812px;top:3400px">Subscribe to our Blog</h4>
  <p class="abs sub-copy">Sign up today to get resources on how to attract and retain more customers!</p>
  <div class="abs sub-form"><span class="ph">✉ Email Address</span>
    <span class="go"><svg width="16" height="16" viewBox="0 0 24 24"><path d="M2 12L22 3l-6 19-4-8z" fill="#000"/></svg></span></div>
  <span class="social" style="left:814px"></span>
  <span class="social" style="left:851px"></span>
  <span class="social" style="left:886px"></span>
  <span class="social" style="left:923px"></span>

  <div class="abs f-rule"></div>
  <p class="abs f-bottom" style="left:143px">Copyright© 2024 <u>KETRAV</u> &nbsp;|&nbsp; All Rights Reserved</p>
  <p class="abs f-bottom" style="left:827px">Terms and Conditions &nbsp; | &nbsp; Privacy Policy</p>
</footer>

</body>
</html>
```